K.O.V Ventures - Business Card

We need a business card design for a new company based in Malaysia, called K.O.V Ventures Sdn. Bhd. We create, develop & customize database & software/web-based business systems to suit our clients need, mainly in oil&gas industry.

We would like to challenge the creativity of you to design a simple, meaningful, modern, professional & sleek. The design concept may varies but worthy enough for the recipients to proudly keep it in their wallet, and award us with fruitful business opportunities.

B-7-12 Lantera Plaza,
PJU9/4, Damai Perdana,
47500 Selangor. Malaysia

http://kovventures-example.com

HAFIZ Rosman | +6012-7038812 | Co-Founder
Di Kamarul | +6012-4190273 | Co-Founder
Amir Syukri | +6019-3306158 | Managing Director

Target Market(s)

The target market will expand to several other industries such as aviation, communication, automotive, education & hotel.

Industry/Entity Type

Business

Font styles to use
Serif
Sans Serif
Decorative
Script

Requirements
Must have
• plain background yet colourful concept.
Should not have
• something too easy that I can draw myself

```html
<!DOCTYPE html>
<html lang="en">
<head>
<meta charset="utf-8">
<title>K.O.V Ventures - Business Card</title>
<link rel="stylesheet" href="https://fonts.googleapis.com/css2?family=Open+Sans:wght@400;700&display=swap">
<style>
  :root {
    --page: #d9d9d9;
    --card: #141414;
    --card-light: #2a2a2a;
    --ink: #f2f2f2;
    --green: #3fc34a;
    --lime: #8fd13f;
    --orange: #ff8a2a;
    --pink: #ff2d6f;
    --magenta: #d62aa0;
    --purple: #7b3fc9;
    --blue: #3a6fd8;
    --teal: #22b8a0;
  }
  * { box-sizing: border-box; margin: 0; padding: 0; }
  html, body { width: 1200px; height: 1040px; overflow: hidden; }
  body {
    background: var(--page);
    font-family: "Open Sans", sans-serif;
    position: relative;
  }
  .card {
    position: absolute;
    top: 95px;
    width: 520px;
    height: 850px;
    overflow: hidden;
    background: radial-gradient(ellipse at 60% 35%, var(--card-light), var(--card) 70%);
    box-shadow: 0 6px 24px rgba(0,0,0,.35);
  }
  .card--front { left: 60px; }
  .card--back { left: 620px; }

  .stripe {
    position: absolute;
    width: 8px;
    border-radius: 1px;
  }
  .stripe--top { top: 0; height: 70px; background: linear-gradient(var(--lime), var(--green)); }
  .stripe--long {
    top: 265px; bottom: 0;
    background: linear-gradient(var(--orange), var(--pink) 30%, var(--magenta) 48%, var(--purple) 62%, var(--blue) 72%, var(--teal) 84%, var(--green));
  }
  .stripe--a { left: 70px; }
  .stripe--b { left: 108px; }

  .brand {
    position: absolute;
    display: flex;
    align-items: center;
    gap: 10px;
    color: var(--ink);
    font-weight: 700;
    white-space: nowrap;
  }
  .brand__dot {
    border-radius: 50%;
    background: var(--pink);
    flex: none;
  }
  .card--front .brand { left: 40px; top: 150px; font-size: 22px; }
  .card--front .brand__dot { width: 40px; height: 40px; }
  .card--back .brand { left: 0; right: 0; top: 390px; justify-content: center; font-size: 30px; }
  .card--back .brand__dot { width: 48px; height: 48px; }

  .contact {
    position: absolute;
    left: 190px;
    top: 430px;
    color: var(--ink);
  }
  .contact__name {
    font-size: 26px;
    font-weight: 700;
    letter-spacing: .5px;
    background: linear-gradient(90deg, var(--green), var(--teal) 22%, var(--blue) 40%, var(--purple) 55%, var(--magenta) 72%, var(--pink));
    -webkit-background-clip: text;
    background-clip: text;
    color: transparent;
  }
  .contact__role { font-size: 19px; margin-top: 2px; }
  .contact__list { list-style: none; margin-top: 42px; }
  .contact__item {
    display: flex;
    gap: 14px;
    font-size: 20px;
    line-height: 1.3;
    margin-bottom: 30px;
  }
  .contact__item svg { flex: none; width: 22px; height: 22px; margin-top: 3px; fill: var(--ink); }
  .contact__item--web { margin-top: 40px; }

  .backdrop {
    position: absolute;
    inset: 0;
    background: radial-gradient(ellipse at 50% 45%, #2c2c2c, #161616 75%);
  }
</style>
</head>
<body>
  <section class="card card--front" aria-label="Card front">
    <span class="stripe stripe--top stripe--a"></span>
    <span class="stripe stripe--top stripe--b"></span>
    <div class="brand"><span class="brand__dot"></span>K.O.V Ventures</div>
    <span class="stripe stripe--long stripe--a"></span>
    <span class="stripe stripe--long stripe--b"></span>

    <div class="contact">
      <p class="contact__name">HAFIZ Rosman</p>
      <p class="contact__role">Co-Founder</p>
      <ul class="contact__list">
        <li class="contact__item">
          <svg viewBox="0 0 24 24" aria-hidden="true"><path d="M6.6 10.8a15.1 15.1 0 0 0 6.6 6.6l2.2-2.2c.3-.3.7-.4 1-.2 1.1.4 2.3.6 3.6.6.6 0 1 .4 1 1V20c0 .6-.4 1-1 1A17 17 0 0 1 3 4c0-.6.4-1 1-1h3.5c.6 0 1 .4 1 1 0 1.3.2 2.5.6 3.6.1.3 0 .7-.2 1z"/></svg>
          <span>+6012-7038812</span>
        </li>
        <li class="contact__item">
          <svg viewBox="0 0 24 24" aria-hidden="true"><path d="M12 3 2 12h3v8h5v-6h4v6h5v-8h3z"/></svg>
          <span>B-7-12 Lantera Plaza,<br>PJU9/4, Damai Perdana,<br>47500 Selangor. Malaysia</span>
        </li>
        <li class="contact__item contact__item--web">
          <svg viewBox="0 0 24 24" aria-hidden="true"><path d="M12 2a10 10 0 1 0 0 20 10 10 0 0 0 0-20zm6.9 6h-2.9a15.6 15.6 0 0 0-1.4-3.6A8 8 0 0 1 18.9 8zM12 4c.8 1.2 1.5 2.5 1.9 4h-3.8c.4-1.5 1.1-2.8 1.9-4zM4.3 14a8.2 8.2 0 0 1 0-4h3.4a16.5 16.5 0 0 0 0 4zm.8 2h2.9c.3 1.3.8 2.5 1.4 3.6A8 8 0 0 1 5.1 16zM8 8H5.1a8 8 0 0 1 4.3-3.6C8.8 5.5 8.3 6.7 8 8zm4 12c-.8-1.2-1.5-2.5-1.9-4h3.8c-.4 1.5-1.1 2.8-1.9 4zm2.3-6H9.7a14.7 14.7 0 0 1 0-4h4.6a14.7 14.7 0 0 1 0 4zm.3 5.6c.6-1.1 1.1-2.3 1.4-3.6h2.9a8 8 0 0 1-4.3 3.6zm1.7-5.6a16.5 16.5 0 0 0 0-4h3.4a8.2 8.2 0 0 1 0 4z"/></svg>
          <span>http://kovventures-example.com</span>
        </li>
      </ul>
    </div>
  </section>

  <section class="card card--back" aria-label="Card back">
    <div class="backdrop" role="img" aria-label="Dark background with a faint repeating brand pattern"></div>
    <div class="brand"><span class="brand__dot"></span>K.O.V Ventures</div>
  </section>
</body>
</html>
```